DESKHAVEN COWORKING Website design and coding

DESKHAVEN COWORKING

DESKHAVEN is Galveston’s first (and currently only) shared business co-working space. We share the same upscale, casual work environment, but we work independently on our own (or our team’s) projects and goals. For only a flat $195 membership fee per month, you have your very own all-inclusive, fun, personal business office environment. Website is written (Word file #12, below); and all pictures etc provided. Galveston is a beachy, coastal, historic city an hour from Houston, Texas USA. Logo (file 11 below) is temporary only.

Target Market(s)

Outside sales people, medical students looking for study hall, Houston companies looking for local office, real estate agents, graphic artists, entrepreneurs, etc

Contact Information for Business Card

will discuss --want to combine with current business card with multiple businesses

Logo Text

DESKHAVEN COWORKING

Coding

Coded - Design and coding required

Number of Pages Required

5+ page

Colors
ec1f27
fbed22

Requirements
Nice to have
• maroon/wine dominant with yellow and red accents, gray base are the colors of the space--website could coordinate--but open to creative ideas/combinations

```html
<!DOCTYPE html>
<html lang="en">
<head>
<meta charset="utf-8">
<title>Deskhaven Coworking – Membership</title>
<link href="https://fonts.googleapis.com/css2?family=Poppins:wght@400;500;600;700&display=swap" rel="stylesheet">
<style>
:root{
  --maroon:#8a0b0b;
  --ink:#222;
  --nav:#2b2b2b;
  --field:#ebebeb;
  --yellow:#fbed22;
  --footer:#1d1f26;
  --footer-map:#252832;
  --white:#fff;
  --red:#c8101a;
  --hero-a:#3f4b6e;
  --hero-b:#8a7a52;
}
*{box-sizing:border-box;margin:0;padding:0}
html,body{width:1116px;height:1200px;overflow:hidden}
body{position:relative;font-family:'Poppins',sans-serif;background:var(--white);color:var(--ink)}
.header{position:absolute;left:0;top:0;width:1116px;height:64px;background:var(--white)}
.brand{position:absolute;left:83px;top:10px;color:var(--maroon);font-weight:700;line-height:1.05;text-align:center}
.brand .line1{font-size:22px;letter-spacing:.5px}
.brand .line2{font-size:14px;letter-spacing:1px}
.nav{position:absolute;right:82px;top:25px;display:flex;gap:32px;font-size:12.5px;color:var(--nav)}
.nav .active{color:var(--maroon)}
.hero{position:absolute;left:0;top:64px;width:1116px;height:167px;background:linear-gradient(100deg,var(--hero-b),var(--hero-a) 55%,#2d3a5e)}
.hero h1{position:absolute;width:100%;top:66px;text-align:center;color:var(--white);font-size:31px;font-weight:700}
.title{position:absolute;left:0;width:1116px;text-align:center}
.title-name{top:320px;font-size:38px;line-height:1;font-weight:700;color:var(--maroon);letter-spacing:1px}
.title-plan{top:360px;font-size:40px;line-height:1;font-weight:700;color:#000;letter-spacing:2px}
.title-price{top:405px;font-size:18px;line-height:1.2;color:#444}
.field{position:absolute;background:var(--field);font-size:13px;font-weight:500;color:#444;padding:12px 18px}
.submit{position:absolute;left:479px;top:689px;width:158px;height:35px;background:var(--yellow);font-size:12.5px;font-weight:700;color:#111;text-align:center;line-height:35px}
.footer{position:absolute;left:0;top:815px;width:1116px;height:385px;background:var(--footer);color:var(--white)}
.map{position:absolute;left:300px;top:20px;width:630px;height:365px;background:radial-gradient(ellipse at center,var(--footer-map),var(--footer) 70%)}
.footer-brand{position:absolute;left:83px;top:165px;color:var(--maroon);font-weight:700;text-align:center;line-height:1.1}
.footer-brand .line1{font-size:30px}
.footer-brand .line2{font-size:20px;letter-spacing:1px}
.col{position:absolute;top:115px;font-size:12px;line-height:16.5px}
.col h3{font-size:14.5px;font-weight:700;margin-bottom:12px;letter-spacing:.3px}
.item{position:relative;padding-left:21px;margin-bottom:9px}
.item svg{position:absolute;left:0;top:2px}
.rule{position:absolute;left:78px;top:332px;width:959px;height:1px;background:#444}
.copy{position:absolute;left:83px;top:350px;font-size:13px;font-weight:500}
.social{position:absolute;top:355px;width:12px;height:12px;border-radius:50%;background:var(--white)}
.totop{position:absolute;left:1048px;top:314px;width:38px;height:38px;border-radius:50%;background:var(--red)}
</style>
</head>
<body>
<header class="header">
  <div class="brand"><div class="line1">DESKHAVEN</div><div class="line2">COWORKING</div></div>
  <nav class="nav"><span>ABOUT</span><span>AMENITIES</span><span class="active">MEMBERSHIP</span><span>GALLERY</span><span>THE DESKHAVEN PHILOSOPHY</span><span>CONTACT</span></nav>
</header>
<section class="hero" role="img" aria-label="Photo of the coworking lounge with tables and yellow chairs">
  <h1>MEMBERSHIP</h1>
</section>
<div class="title title-name">Deskhaven</div>
<div class="title title-plan">MEMBERSHIP</div>
<div class="title title-price">For only $195 a month</div>
<div class="field" style="left:306px;top:449px;width:250px;height:40px">Name</div>
<div class="field" style="left:560px;top:449px;width:251px;height:40px">Address</div>
<div class="field" style="left:306px;top:495px;width:250px;height:40px">Phone number</div>
<div class="field" style="left:560px;top:495px;width:251px;height:40px">Email</div>
<div class="field" style="left:306px;top:543px;width:505px;height:133px">Description of business</div>
<div class="submit">SUBMIT NOW</div>
<footer class="footer">
  <div class="map" role="img" aria-label="Dotted world map background"></div>
  <div class="footer-brand"><div class="line1">DESKHAVEN</div><div class="line2">COWORKING</div></div>
  <div class="col" style="left:350px">
    <h3>CONTACT US</h3>
    <div class="item"><svg width="12" height="10" viewBox="0 0 12 10"><rect width="12" height="10" fill="#fbed22"/><path d="M0 0l6 5 6-5" stroke="#1d1f26" fill="none"/></svg>Email:<br>hello@deskhavenwork.com</div>
    <div class="item"><svg width="12" height="12" viewBox="0 0 12 12"><path d="M2 0l3 3-1.5 1.5a7 7 0 0 0 4 4L9 7l3 3-2 2C5 12 0 7 0 2z" fill="#fbed22"/></svg>Phone:<br>888-555-0142</div>
  </div>
  <div class="col" style="left:603px">
    <h3>PHYSICAL LOCATION</h3>
    <div class="item"><svg width="10" height="13" viewBox="0 0 10 13"><path d="M5 0a5 5 0 0 1 5 5c0 3-5 8-5 8S0 8 0 5a5 5 0 0 1 5-5z" fill="#fbed22"/><circle cx="5" cy="5" r="2" fill="#1d1f26"/></svg>Deskhaven Coworking<br>418 Harbor Ave, Suite 12<br>Galveston, TX 77550</div>
  </div>
  <div class="col" style="left:813px">
    <h3>OWNER</h3>
    <div style="margin-bottom:12px;font-weight:500">Harlow Interests</div>
    <div class="item"><svg width="12" height="10" viewBox="0 0 12 10"><rect width="12" height="10" fill="#fbed22"/><path d="M0 0l6 5 6-5" stroke="#1d1f26" fill="none"/></svg>office@harlowinterests.com</div>
    <div class="item"><svg width="12" height="12" viewBox="0 0 12 12"><path d="M2 0l3 3-1.5 1.5a7 7 0 0 0 4 4L9 7l3 3-2 2C5 12 0 7 0 2z" fill="#fbed22"/></svg>713-555-0187</div>
    <div class="item"><svg width="10" height="13" viewBox="0 0 10 13"><path d="M5 0a5 5 0 0 1 5 5c0 3-5 8-5 8S0 8 0 5a5 5 0 0 1 5-5z" fill="#fbed22"/><circle cx="5" cy="5" r="2" fill="#1d1f26"/></svg>Harlow Interests<br>95 Linden St., Suite 300<br>Houston, TX 77002</div>
  </div>
  <div class="rule"></div>
  <div class="copy">Copyright © 2020, Deskhaven Coworking. All Rights Reserved</div>
  <span class="social" style="left:936px"></span>
  <span class="social" style="left:979px"></span>
  <span class="social" style="left:1019px"></span>
  <div class="totop"><svg width="38" height="38" viewBox="0 0 38 38"><path d="M19 26V12M14 17l5-5 5 5" stroke="#fff" stroke-width="1.5" fill="none"/></svg></div>
</footer>
</body>
</html>
```